Show Me Your Best Ideas, Design a Whisky Label

We need a front label only for a whisky bottle. The label is to be used as a mockup for a product idea.
The design needs to be presented as a 3D render on the 'Product Bottle' image supplied. We will print the image of the bottle.

This label is for a Graduation in 2020. Emphasis should be placed on the word Graduation and the date: 2020.

Text:
Graduation
2020
Single Malt Whisky
Northvale Service Cadet College

Target Market(s)

20-25 year old

Font styles to use
Serif
Sans Serif
Decorative

Colors

Designer to choose colors to be used in the design.

Requirements
Must have
• 3D render of finished design

```html
<!DOCTYPE html>
<html lang="en">
<head>
<meta charset="utf-8">
<title>Graduation 2020 Single Malt Whiskey Label</title>
<link rel="stylesheet" href="https://fonts.googleapis.com/css2?family=Pinyon+Script&family=Cormorant+Garamond:wght@600&family=Montserrat:wght@600;700&display=swap">
<style>
  :root {
    --page: #ffffff;
    --navy: #0c1f4d;
    --gold: #e3cf8a;
    --gold-deep: #c9ae5e;
    --cream: #f3ecd2;
  }
  * { margin: 0; padding: 0; box-sizing: border-box; }
  html, body {
    width: 1200px;
    height: 1000px;
    overflow: hidden;
    background: var(--page);
  }
  .canvas {
    width: 1200px;
    height: 1000px;
    display: flex;
    align-items: center;
    justify-content: center;
  }
  .label {
    position: relative;
    width: 580px;
    height: 580px;
    background: var(--navy);
    border: 6px solid var(--gold);
    box-shadow: inset 0 0 0 4px var(--navy), inset 0 0 0 5px var(--gold-deep);
    display: flex;
    flex-direction: column;
    align-items: center;
    text-align: center;
    color: var(--gold);
  }
  .college-mark {
    margin-top: 46px;
    height: 210px;
    display: flex;
    flex-direction: column;
    align-items: center;
    justify-content: center;
    gap: 18px;
  }
  .college-mark__dot {
    width: 70px;
    height: 70px;
    border-radius: 50%;
    background: var(--gold);
  }
  .college-mark__name {
    font-family: "Montserrat", sans-serif;
    font-weight: 600;
    font-size: 20px;
    letter-spacing: 3px;
    text-transform: uppercase;
    color: var(--gold);
    line-height: 1.4;
    max-width: 360px;
  }
  .title {
    margin-top: 16px;
    font-family: "Pinyon Script", cursive;
    font-weight: 400;
    font-size: 104px;
    line-height: 1;
    color: var(--gold);
  }
  .year {
    margin-top: 4px;
    font-family: "Cormorant Garamond", serif;
    font-weight: 600;
    font-size: 64px;
    line-height: 1;
    letter-spacing: 2px;
    color: var(--cream);
  }
  .style {
    margin-top: 34px;
    font-family: "Montserrat", sans-serif;
    font-weight: 600;
    font-size: 17px;
    letter-spacing: 4px;
    color: var(--cream);
  }
  .spirit {
    margin-top: 8px;
    font-family: "Montserrat", sans-serif;
    font-weight: 700;
    font-size: 22px;
    letter-spacing: 4px;
    color: var(--cream);
  }
</style>
</head>
<body>
  <main class="canvas">
    <section class="label">
      <div class="college-mark">
        <span class="college-mark__dot"></span>
        <p class="college-mark__name">Northvale Service Cadet College</p>
      </div>
      <h1 class="title">Graduation</h1>
      <p class="year">2020</p>
      <p class="style">SINGLE MALT</p>
      <p class="spirit">WHISKEY</p>
    </section>
  </main>
</body>
</html>
```